RK Website Home Page Design

The task is to develop a winning design for a replacement website for our client RK Plumbing, Heating, AC & Remodeling. ct

```html
<!DOCTYPE html>
<html lang="en">
<head>
<meta charset="utf-8">
<title>RK Plumbing, Heating, AC &amp; Remodeling</title>
<link href="https://fonts.googleapis.com/css2?family=Poppins:wght@400;600;700&family=Roboto:wght@400;500;700&display=swap" rel="stylesheet">
<style>
:root{
  --yellow:#e6ee12;
  --yellow-soft:#f4f8a0;
  --olive:#8a8a6a;
  --olive-light:#d9d9cc;
  --ink:#111111;
  --dark:#1b1b1b;
  --text:#333333;
  --muted:#666666;
  --white:#ffffff;
}
*{box-sizing:border-box;margin:0;padding:0}
html,body{width:1200px;height:4286px;overflow:hidden}
body{position:relative;font-family:'Roboto',sans-serif;color:var(--text);background:linear-gradient(#8c8c6c 600px,#e9e9e0 1150px,#fff 1300px)}
.abs{position:absolute}
a{color:inherit}

/* header & hero */
.hero{left:0;top:0;width:1200px;height:600px;background:linear-gradient(110deg,#2a2a20 0%,#5e5a2c 45%,#b3b028 70%,#5a5a3a 100%)}
.brand{left:62px;top:30px;width:190px;height:70px;display:flex;align-items:center;gap:8px;color:var(--white);font:700 17px 'Roboto',sans-serif}
.brand i{width:14px;height:14px;background:var(--yellow);display:block}
.topline{left:435px;top:20px;color:var(--white);font:500 17px 'Roboto',sans-serif}
.top-btn{top:20px;height:22px;padding:0 10px;border:1px solid var(--yellow);color:var(--yellow);font:13px 'Roboto',sans-serif;line-height:20px}
.top-btn.fill{background:var(--yellow);color:#333}
.nav{left:303px;top:72px;display:flex;gap:23px;color:var(--white);font:13px 'Roboto',sans-serif}
.hero-panel{left:38px;top:148px;width:640px;height:452px;background:rgba(20,20,20,.72)}
.hero h1{left:83px;top:188px;font:700 56px/76px 'Poppins',sans-serif;color:var(--white)}
.hero h1 span{color:var(--yellow)}
.hero .sub{left:83px;top:352px;font:400 34px 'Poppins',sans-serif;color:var(--yellow)}
.hero .cta{left:83px;top:466px;color:var(--yellow);font:500 20px 'Roboto',sans-serif;display:flex;gap:10px;align-items:center}
.hero .phones{left:120px;top:503px;color:var(--white);font:700 19px/26px 'Roboto',sans-serif}

/* services */
.section-title{width:1200px;left:0;text-align:center;font:500 29px 'Roboto',sans-serif;color:var(--white)}
.underline{width:220px;height:3px;left:490px;background:var(--yellow)}
.watermark{left:60px;top:830px;width:1080px;font:700 130px 'Roboto',sans-serif;color:rgba(255,255,255,.1);letter-spacing:6px}
.svc{width:118px;height:133px;border-radius:14px;background:linear-gradient(#fff 10%,var(--yellow) 100%);box-shadow:0 4px 8px rgba(0,0,0,.25);text-align:center;font:13px/15px 'Roboto',sans-serif;color:#333}
.svc .ico{width:70px;height:70px;margin:14px auto 8px;border-radius:50%;background:var(--ink);display:flex;align-items:center;justify-content:center}
.svc span{text-decoration:underline}

/* form */
.request{left:253px;top:1200px;width:694px;height:539px;background:var(--dark);border-radius:24px;box-shadow:0 6px 10px rgba(0,0,0,.3)}
.request h2{position:absolute;width:100%;top:34px;text-align:center;color:var(--white);font:400 31px 'Roboto',sans-serif}
.request h2 span{color:var(--yellow)}
.field{position:absolute;height:34px;border:1px solid #ccc;color:#ddd;font:12px 'Roboto',sans-serif;padding:10px}
.submit{position:absolute;left:286px;top:478px;width:122px;height:32px;background:var(--yellow);color:#111;text-align:center;font:15px/32px 'Roboto',sans-serif}

/* school band */
.school{left:0;top:1859px;width:1200px;height:354px;background:linear-gradient(90deg,#7e7e5e 0%,#b4b49e 60%,#e4e4dc 100%)}
.school-photo{left:713px;top:1850px;width:487px;height:363px;background:linear-gradient(135deg,#6b5a48,#c9a26a 55%,#8a6d4a)}
.school h3{left:28px;top:1900px;color:var(--white);font:500 29px 'Roboto',sans-serif}
.school p{left:28px;top:1998px;width:720px;color:var(--white);font:17px/33px 'Roboto',sans-serif}
.school p a{color:var(--yellow)}
.school .big{left:28px;top:2122px;color:var(--yellow);font:29px 'Roboto',sans-serif;text-decoration:underline}

/* difference */
.diff-frame{left:60px;top:2321px;width:601px;height:441px;background:var(--yellow);border-radius:24px;transform:rotate(-1.5deg)}
.diff-photo{left:62px;top:2343px;width:598px;height:400px;border-radius:20px;background:linear-gradient(120deg,#3a3f42,#8b8f8e 50%,#55504a)}
.diff h3{left:720px;top:2402px;font:700 31px 'Roboto',sans-serif;color:var(--ink)}
.diff p{left:720px;top:2460px;width:450px;font:14px/26.5px 'Roboto',sans-serif;color:var(--muted)}
.pill{background:linear-gradient(#fff 30%,var(--yellow));border-radius:18px;text-align:center;box-shadow:0 3px 5px rgba(0,0,0,.25)}
.learn{left:720px;top:2696px;width:182px;height:38px;font:17px/38px 'Roboto',sans-serif;color:#333}

/* savings */
.savings-bg{left:0;top:2884px;width:1200px;height:470px;background:linear-gradient(#7f7f60,#e6e6de 90%,#fff)}
.savings-title{left:0;top:2956px;width:1200px;text-align:center;color:var(--white);font:500 30px 'Roboto',sans-serif}
.savings-title span{color:var(--yellow)}
.deal{top:3023px;width:240px;height:258px;border-radius:12px;background:linear-gradient(160deg,#4a4d52,#1e2024);color:var(--white);text-align:center}
.tag{position:absolute;left:-4px;top:4px;width:110px;height:64px;background:var(--yellow);transform:rotate(-35deg);transform-origin:left top;font:700 15px/18px 'Roboto',sans-serif;color:#111;padding:10px 0 0 30px;text-align:left;margin-top:60px}
.deal p{position:absolute;top:120px;width:100%;font:500 18px/27px 'Roboto',sans-serif;padding:0 20px}
.deal .go{position:absolute;left:54px;top:218px;width:132px;height:26px;background:var(--yellow);opacity:.75;border-radius:13px;font:13px/26px 'Roboto',sans-serif;color:#fff}

/* blog */
.blog-title{left:0;top:3402px;width:1200px;text-align:center;font:500 29px 'Roboto',sans-serif;color:var(--ink)}
.post{top:3479px;width:361px;height:301px;box-shadow:0 3px 6px rgba(0,0,0,.3)}
.post .img{position:absolute;inset:0}
.post .cap{position:absolute;left:0;bottom:0;width:100%;height:83px;background:rgba(15,15,15,.75);padding:16px 16px}
.post h4{color:var(--white);font:500 18px 'Roboto',sans-serif;text-decoration:underline}
.post small{display:block;margin-top:14px;color:var(--yellow);font:9px 'Roboto',sans-serif}
.viewmore{left:519px;top:3832px;width:162px;height:34px;border-radius:0;font:15px/34px 'Roboto',sans-serif;color:#333}

/* footer */
.footer{left:0;top:3960px;width:1200px;height:326px;background:#000}
.fcol{top:3993px;color:var(--white)}
.fcol h5{font:500 12px 'Roboto',sans-serif;color:var(--yellow);margin-bottom:8px}
.fcol li{list-style:none;font:6.5px/11.5px 'Roboto',sans-serif}
.fcol li::before{content:"• "}
.fcontact{left:1020px;top:3993px;color:var(--white);font:500 9px/16px 'Roboto',sans-serif}
.fcontact h5{font:500 13px 'Roboto',sans-serif;color:var(--yellow);margin-bottom:10px}
.fbrand{left:62px;top:4168px;color:var(--white);font:700 22px 'Roboto',sans-serif;display:flex;align-items:center;gap:10px}
.fbrand i{width:18px;height:18px;background:var(--yellow);display:block}
.social{top:4200px;width:28px;height:28px;border-radius:50%;background:var(--yellow)}
.card{top:4225px;width:60px;height:28px;background:var(--white);border-radius:3px}
.copy{left:0;top:4260px;width:1200px;text-align:center;color:#777;font:9px 'Roboto',sans-serif}
</style>
</head>
<body>

<!-- hero -->
<section class="abs hero" role="img" aria-label="Photo of a woman dancing in a bright modern living room"></section>
<div class="abs brand"><i></i>RK Plumbing</div>
<div class="abs topline">Serving Maple Falls, MA &amp; Neighboring Communities</div>
<div class="abs top-btn fill" style="left:886px">Request Service</div>
<div class="abs top-btn" style="left:1024px">Request a qoute</div>
<nav class="abs nav"><span>ABOUT</span><span>Plumbing ▾</span><span>Water Heaters ▾</span><span>Heating ▾</span><span>Air conditioning ▾</span><span>Indoor air quality ▾</span><span>Handy work&amp;Remodeling ▾</span><span>Commercial ▾</span></nav>
<div class="abs hero-panel"></div>
<h1 class="abs hero-h" style="position:absolute"></h1>
<div class="abs" style="left:83px;top:188px;font:700 56px/76px 'Poppins',sans-serif;color:#fff"><span style="color:var(--yellow)">Enjoy</span> The Best<br>Of Home Living.</div>
<div class="abs" style="left:83px;top:352px;font:400 34px 'Poppins',sans-serif;color:var(--yellow)">Indoors &amp; Out.</div>
<div class="abs" style="left:83px;top:466px;color:var(--yellow);font:500 20px 'Roboto',sans-serif;display:flex;gap:10px;align-items:center">
  <svg width="20" height="20" viewBox="0 0 24 24" fill="none" stroke="#e6ee12" stroke-width="2"><path d="M22 16.9v3a2 2 0 0 1-2.2 2 19.8 19.8 0 0 1-8.6-3.1 19.5 19.5 0 0 1-6-6A19.8 19.8 0 0 1 2.1 4.2 2 2 0 0 1 4.1 2h3a2 2 0 0 1 2 1.7c.1 1 .4 1.9.7 2.8a2 2 0 0 1-.5 2.1L8 9.9a16 16 0 0 0 6 6l1.3-1.3a2 2 0 0 1 2.1-.4c.9.3 1.8.6 2.8.7a2 2 0 0 1 1.7 2z"/></svg>
  <span style="text-decoration:underline">Contact Us to Get Started!</span></div>
<div class="abs" style="left:120px;top:503px;color:#fff;font:700 19px/26px 'Roboto',sans-serif">800.555.0142<br>508.555.0187</div>

<!-- services -->
<div class="abs watermark">RK PLUMBING</div>
<h2 class="abs section-title" style="top:660px">More of What You Need</h2>
<div class="abs underline" style="top:706px"></div>

<div class="abs svc" style="left:235px;top:782px"><div class="ico"><svg width="40" height="40" viewBox="0 0 24 24" fill="none" stroke="#e6ee12" stroke-width="2.4"><path d="M5 19l9-9M14 5l5 5-3 3-5-5z"/></svg></div><span>Plumbing</span></div>
<div class="abs svc" style="left:439px;top:782px"><div class="ico"><svg width="40" height="40" viewBox="0 0 24 24" fill="none" stroke="#e6ee12" stroke-width="2.4"><rect x="7" y="3" width="10" height="18" rx="3"/><circle cx="12" cy="9" r="2"/></svg></div><span>Water Heaters</span></div>
<div class="abs svc" style="left:642px;top:782px"><div class="ico"><svg width="40" height="40" viewBox="0 0 24 24" fill="none" stroke="#e6ee12" stroke-width="2.4"><path d="M5 6h14M5 10h14M5 14h14M5 18h14"/></svg></div><span>Heating</span></div>
<div class="abs svc" style="left:847px;top:782px"><div class="ico"><svg width="40" height="40" viewBox="0 0 24 24" fill="none" stroke="#e6ee12" stroke-width="2.4"><path d="M12 12l-5-6M12 12l5-6M12 12v-2M12 12l-6 4M12 12l6 4"/></svg></div><span>Air Conditioning</span></div>
<div class="abs svc" style="left:235px;top:973px"><div class="ico"><svg width="40" height="40" viewBox="0 0 24 24" fill="none" stroke="#e6ee12" stroke-width="2.4"><path d="M6 6h12M6 10h12M6 14h12M6 18h12"/></svg></div><span>Water Filtration</span></div>
<div class="abs svc" style="left:439px;top:973px"><div class="ico"><svg width="40" height="40" viewBox="0 0 24 24" fill="none" stroke="#e6ee12" stroke-width="2.4"><path d="M4 20l10-10M12 4l8 8-3 3-8-8z"/></svg></div><span>Remodeling &amp;<br>Handy Work</span></div>
<div class="abs svc" style="left:642px;top:973px"><div class="ico"><svg width="40" height="40" viewBox="0 0 24 24" fill="none" stroke="#e6ee12" stroke-width="2.4"><path d="M5 20V9a7 7 0 0 1 14 0v11zM12 17c-2 0-3-1.5-2-3.5l2-3 2 3c1 2 0 3.5-2 3.5z"/></svg></div><span>Gas Fireplaces</span></div>
<div class="abs svc" style="left:847px;top:973px"><div class="ico"><svg width="40" height="40" viewBox="0 0 24 24" fill="none" stroke="#e6ee12" stroke-width="2.4"><path d="M4 6c6 2 10 6 14 12M4 11c5 1 8 4 11 8M9 4c4 3 7 7 10 12"/></svg></div><span>Indoor Air<br>Quality</span></div>

<!-- request form -->
<form class="abs request">
  <h2>Request <span>service</span></h2>
  <div class="field" style="left:47px;top:107px;width:274px">*Name:</div>
  <div class="field" style="left:380px;top:107px;width:268px">Address:</div>
  <div class="field" style="left:47px;top:164px;width:274px">City:</div>
  <div class="field" style="left:380px;top:164px;width:268px">Zip:</div>
  <div class="field" style="left:47px;top:220px;width:274px">*Email:</div>
  <div class="field" style="left:377px;top:220px;width:271px">Phone:</div>
  <div class="field" style="left:47px;top:292px;width:601px;height:140px">message...</div>
  <div class="submit">Submit</div>
</form>

<!-- back to school -->
<section class="abs school"></section>
<div class="abs school-photo" role="img" aria-label="Photo of a mother and two children preparing lunches at a kitchen table"></div>
<h3 class="abs" style="left:28px;top:1902px;color:#fff;font:500 29px 'Roboto',sans-serif">Back to School Reminder!
  <svg width="30" height="30" viewBox="0 0 24 24" fill="#e6ee12" style="vertical-align:-4px;margin-left:10px"><path d="M12 2a6 6 0 0 0-6 6v5l-2 3h16l-2-3V8a6 6 0 0 0-6-6zM10 19a2 2 0 0 0 4 0z"/></svg></h3>
<p class="abs" style="left:28px;top:1998px;width:730px;color:#fff;font:17px/33px 'Roboto',sans-serif">Most families see an uptick in morning “rush hour” activity once the school year begins, and so does your water heater. Can yours keep up with the increased demand? <a style="color:var(--yellow)">Contact us</a> today for a water heater check-up and</p>
<a class="abs" style="left:28px;top:2122px;color:var(--yellow);font:29px 'Roboto',sans-serif">free quote on a replacement system.</a>

<!-- difference -->
<div class="abs diff-frame"></div>
<div class="abs diff-photo" role="img" aria-label="Photo of a woman relaxing on a sofa with her dog by candlelight"></div>
<h3 class="abs" style="left:720px;top:2402px;font:700 31px 'Roboto',sans-serif;color:var(--ink)">The RK difference maker</h3>
<p class="abs" style="left:720px;top:2460px;width:450px;font:14px/26.5px 'Roboto',sans-serif;color:var(--muted)">RK is a favorite choice among homeowners who appreciate our extensive range of home comfort and related services. Others like us best for our 100% satisfaction guarantee, while still others enjoy the many benefits that membership in our Preferred Service Club provides. Add it all up, and there’s a lot to like about RK Plumbing, Heating, AC &amp; Remodeling.</p>
<div class="abs pill learn">Learn more</div>

<!-- savings -->
<section class="abs savings-bg"></section>
<h2 class="abs savings-title">Enjoy the <span>Savings</span>...Plus the Added Comfort!</h2>
<div class="abs deal" style="left:180px" role="img" aria-label="Photo of a water heater"><div class="tag">SAVE<br>$120</div><p>on a new water heater, tank-style or tankless</p><div class="go">Click for details</div></div>
<div class="abs deal" style="left:482px" role="img" aria-label="Photo of heating and cooling equipment"><div class="tag">SAVE<br>$350</div><p>on a new heating or cooling system.</p><div class="go">Click for details</div></div>
<div class="abs deal" style="left:785px" role="img" aria-label="Photo of a handshake"><div class="tag">SAVE<br>$35</div><p>on any service we provide.</p><div class="go">Click for details</div></div>

<!-- blog -->
<h2 class="abs blog-title">Latest Blog Feeds</h2>
<article class="abs post" style="left:40px"><div class="img" role="img" aria-label="Photo of a coral-toned dining room" style="background:linear-gradient(135deg,#b86a5c,#6d4a40)"></div><div class="cap"><h4>The Benefits of an AC Tune-Up</h4><small>● rk-admin &nbsp;&nbsp; ◷ MAY 19 2023</small></div></article>
<article class="abs post" style="left:423px"><div class="img" role="img" aria-label="Photo of a modern bathroom with a blue wall" style="background:linear-gradient(135deg,#d8dcdf,#4c93c2 50%,#777)"></div><div class="cap"><h4>How to Choose the Best Toilet Style</h4><small>● rk-admin &nbsp;&nbsp; ◷ APRIL 27 2023</small></div></article>
<article class="abs post" style="left:805px"><div class="img" role="img" aria-label="Photo of an empty white room with a ductless air unit" style="background:linear-gradient(135deg,#f1f1f1,#b8b8b8)"></div><div class="cap"><h4>Beat the Summer Heat withDuctless Air</h4><small>● rk-admin &nbsp;&nbsp; ◷ APRIL 13 2023</small></div></article>
<div class="abs pill viewmore">View more &nbsp;→</div>

<!-- footer -->
<footer class="abs footer"></footer>
<div class="abs fcol" style="left:57px"><h5>ABOUT US</h5><ul><li>Company Profile</li><li>Guarantees &amp; Assurances</li><li>Priority Service Club</li><li>Employment</li><li>Areas Served</li></ul></div>
<div class="abs fcol" style="left:172px"><h5>Plumbing</h5><ul><li>Service &amp; Repair</li><li>Plumbing Installations</li><li>Outdoor Plumbing</li><li>Sewer &amp; Drain</li><li>Frozen Pipes</li><li>Gas Piping</li><li>Sump Pumps</li><li>Water Leak Detection &amp; Repair</li><li>Gas Piping</li></ul></div>
<div class="abs fcol" style="left:280px"><h5>Water Heaters</h5><ul><li>Service &amp; Repair</li><li>Tank-style Water Heater</li><li>Tankless Water Heater</li><li>Combi Boiler</li></ul></div>
<div class="abs fcol" style="left:417px"><h5>Heating</h5><ul><li>Preventive Maintenance</li><li>Boiler Service &amp; Repair</li><li>Furnace Service &amp; Repair</li><li>Boiler</li><li>Furnace</li><li>Gas Fireplace Insert</li><li>Ductless Air System</li><li>Combi boiler</li></ul></div>
<div class="abs fcol" style="left:557px"><h5>Handy Work &amp; Remodeling</h5><ul><li>Overview</li><li>Bathroom</li><li>Kitchens</li><li>Decks, Porches &amp; Patios</li><li>Basement</li><li>Windows &amp; Doors</li><li>Gas Fireplace</li><li>Interior &amp; Exterior</li><li>Handyman Services</li></ul></div>
<div class="abs fcol" style="left:759px"><h5>Air Conditioning</h5><ul><li>Preventive Maintenance</li><li>Service &amp; Repair</li><li>New AC System</li><li>Ductless Air System</li></ul>
  <h5 style="margin-top:40px">Indoor Air Quality</h5><ul><li>Air Cleaners</li><li>Duct Sealing</li><li>Humidity Control</li></ul></div>
<div class="abs fcol" style="left:902px"><h5>Commercial</h5><ul><li>Plumbing</li><li>HVAC</li></ul></div>
<div class="abs fcontact"><h5>Contact Us</h5>
  <div style="display:flex;gap:8px"><svg width="14" height="18" viewBox="0 0 24 24" fill="#e6ee12"><path d="M12 2a7 7 0 0 0-7 7c0 5 7 13 7 13s7-8 7-13a7 7 0 0 0-7-7zm0 9.5A2.5 2.5 0 1 1 12 6.5a2.5 2.5 0 0 1 0 5z"/></svg><span>18 Orchard Lane<br>Maple Falls, MA 01999</span></div>
  <div style="display:flex;gap:8px;margin-top:14px"><svg width="14" height="18" viewBox="0 0 24 24" fill="#e6ee12"><path d="M6.6 10.8a15 15 0 0 0 6.6 6.6l2.2-2.2a1 1 0 0 1 1-.2 11 11 0 0 0 3.6.6 1 1 0 0 1 1 1V20a1 1 0 0 1-1 1A17 17 0 0 1 3 4a1 1 0 0 1 1-1h3.5a1 1 0 0 1 1 1 11 11 0 0 0 .6 3.6 1 1 0 0 1-.3 1z"/></svg><span>508.555.0187<br>800.555.0142</span></div></div>
<div class="abs fbrand"><i></i>RK Plumbing</div>
<div class="abs social" style="left:560px"></div>
<div class="abs social" style="left:604px"></div>
<div class="abs card" style="left:920px"></div>
<div class="abs card" style="left:975px;width:38px"></div>
<div class="abs card" style="left:1020px;width:40px"></div>
<div class="abs card" style="left:1066px;width:74px"></div>
<div class="abs copy">@ 2023 RK Heating &amp; Plumbing, All Rights Reserved</div>

</body>
</html>
```